Travel Group 'Halvard Group' needs a new business card design

Halvard Group is a diverse business specialising in bespoke, tailor made holidays to suit all budgets and we are specialists in planning exciting day/short trips to suit all markets. Our target market is very varied going from the corporate client and as well as people in the community who simply want to experience something special.
We are looking for a card design that will encourage people to look at our websites and social media platforms and to see for themselves the different facets to our business. It is essential that the card has social media icons for Pagebloom, Quibbly and Snapverse. We are looking for a card with a blank background with no pictures and for the front side to have the attached Halvard logo. The card should have similar colour scheme to the attached Halvard logo.
The card must have the following information on one side:
Maren Doyle
Business Development Manager
marendoyle@halvardtravel.example
Halvard Group, 48 Fenwick Row
Brackenfold, Westmere, Northvale KB27 4RT
+44 (0)1632 960418
And then the card must have the following on the second side:
(Halvard logo)
(social media icons)
www.halvardtravel.example
www.halvardexperience.example
Target Market(s)
Our target market is very varied going from the corporate client and as well as people in the community who simply want to experience something special.
Industry/Entity Type
Business
Contact Information for Business Card
Maren Doyle
+44 (0)1632 960418
(Halvard logo)
(social media icons)
www.halvardtravel.example
www.halvardexperience.example
Requirements
Must have
- It is essential that the card has social media icons for Pagebloom, Quibbly & Snapverse.
Should not have
- Should not have any images other than Halvard logo.

```html
<!DOCTYPE html>
<html lang="en">
<head>
<meta charset="utf-8">
<title>Halvard Group — Business Card</title>
<link rel="stylesheet" href="https://fonts.googleapis.com/css2?family=Cormorant+Garamond:wght@500;600;700&display=swap">
<style>
  :root {
    --navy: #2a1f5f;
    --purple: #6b3f9c;
    --magenta: #e23d93;
    --paper: #ffffff;
    --backdrop: #ffffff;
    --shadow: rgba(0, 0, 0, 0.28);
  }
  * { box-sizing: border-box; margin: 0; padding: 0; }
  html, body {
    width: 1200px; height: 1200px; overflow: hidden;
    background: var(--backdrop);
    font-family: "Cormorant Garamond", Georgia, serif;
  }
  .sheet { position: relative; width: 1200px; height: 1200px; }
  .card {
    position: absolute; left: 181px; width: 853px; height: 489px;
    background: var(--paper);
    box-shadow: 6px 6px 10px var(--shadow);
  }
  .card--front { top: 58px; }
  .card--back { top: 634px; }

  .wordmark {
    position: absolute; color: var(--navy); font-weight: 700;
    letter-spacing: 0.06em; text-transform: uppercase; line-height: 1;
    white-space: nowrap; transform: translate(-50%, -50%);
  }
  .card--front .wordmark { left: 426px; top: 228px; font-size: 52px; }
  .card--back .wordmark { left: 186px; top: 155px; font-size: 30px; }

  .links {
    position: absolute; left: 0; right: 0; top: 424px;
    display: flex; align-items: center; justify-content: space-between;
    padding: 0 46px 0 56px;
  }
  .url { color: var(--purple); font-weight: 600; font-size: 23px; white-space: nowrap; }
  .socials { display: flex; gap: 12px; }
  .social { display: flex; flex-direction: column; align-items: center; gap: 3px; }
  .social__dot { width: 27px; height: 27px; border-radius: 50%; background: var(--magenta); }
  .social__name { color: var(--magenta); font-weight: 600; font-size: 11px; line-height: 1; }

  .details { position: absolute; left: 378px; top: 104px; color: var(--purple); }
  .details__name {
    color: var(--magenta); font-weight: 700; font-size: 37px; line-height: 1;
    text-transform: uppercase; letter-spacing: 0.01em;
  }
  .details__role, .details__email { font-weight: 600; font-size: 21px; line-height: 28px; }
  .details__role { margin-top: 2px; }
  .address { position: absolute; left: 378px; top: 280px; color: var(--purple);
    font-weight: 500; font-size: 20px; line-height: 29px; font-style: normal; }
  .address__phone { margin-top: 22px; }
</style>
</head>
<body>
<main class="sheet">
  <section class="card card--front" aria-label="Card front">
    <div class="wordmark">Halvard</div>
    <div class="links">
      <span class="url">www.halvardtravel.example</span>
      <div class="socials">
        <div class="social"><span class="social__dot"></span><span class="social__name">Pagebloom</span></div>
        <div class="social"><span class="social__dot"></span><span class="social__name">Quibbly</span></div>
        <div class="social"><span class="social__dot"></span><span class="social__name">Snapverse</span></div>
      </div>
      <span class="url">www.halvardexperience.example</span>
    </div>
  </section>

  <section class="card card--back" aria-label="Card back">
    <div class="wordmark">Halvard</div>
    <div class="details">
      <h1 class="details__name">Maren Doyle</h1>
      <p class="details__role">Business Development Manager</p>
      <p class="details__email">marendoyle@halvardtravel.example</p>
    </div>
    <address class="address">
      <p>Halvard Group, 48 Fenwick Row</p>
      <p>Brackenfold, Westmere, Northvale KB27 4RT</p>
      <p class="address__phone">+44 (0)1632 960418</p>
    </address>
  </section>
</main>
</body>
</html>
```